Web and Logo Design for New Storevane T-shirt Store

I am opening a new online company called Torvelin to sell T-shirts. The website is torvelin.example. For the Menu heading it will be Home, Women, Men, About, Contact, Catalog. For the Categories, it will be Women, Men, T-shirt- Hoodies, Tank Tops, Long Sleeves. I will also need tshirt mockups for the landing page. Footer Menu: Home, About, Contact, Catalog, Shipping and Returns.
The colors to use for the website is #1D7D9E, #Black, #FBC326. For the logo, I will upload examples.
Heading Font: Calistoga.
Body Font: Raleway
Logo Font: Christopher Done.

HERE is an example of how I want my website: mandrel.example, zix.example, frenlo.example, printhollow.example, teeweaver.example.

Target Market(s)

Young people

Industry/Entity Type

Clothing

Coding

Coded - Design and coding required

Number of Pages Required

5+ page

Font styles to use
Sans Serif
Decorative

Colors

Designer to choose colors to be used in the design.

Requirements
Must have
• A unique and creative logo and a stunning homepage.Please look at my website so that you have a feel of what I would like. I want my desgin to have the same page setup as my website.
The colors to use for the website is #1D7D9E, #Black, #FBC326.
Please Look at this link for example: https://shopcrate-lumatheme.storefront.example/
Nice to have
• Tshirt mockups for the homepage, Well use of colors, a homepage slider. A search box.
Should not have
• Don't use basic designs.

```html
<!DOCTYPE html>
<html lang="en">
<head>
<meta charset="utf-8">
<title>Torvelin – Order #1234</title>
<link href="https://fonts.googleapis.com/css2?family=Calistoga&family=Raleway:wght@400;500;600;700&display=swap" rel="stylesheet">
<style>
:root{
  --brand-blue:#1D7D9E;
  --brand-yellow:#FBC326;
  --ink:#000;
  --text:#333;
  --muted:#555;
  --soft:#f3f3f3;
  --line:#e6e6e6;
  --footer:#333333;
  --white:#fff;
}
*{box-sizing:border-box;margin:0;padding:0}
html,body{width:1199px;height:1200px;overflow:hidden}
body{position:relative;font-family:"Raleway",sans-serif;color:var(--text);background:var(--white)}
.abs{position:absolute}
.heading{font-family:"Calistoga",serif;font-weight:400;color:var(--ink)}

.topbar{left:0;top:0;width:1199px;height:37px;background:var(--ink);color:var(--white);font-size:13px}
.topbar .welcome{left:163px;top:11px}
.topbar .help{right:162px;top:11px;display:flex;align-items:center;gap:6px}
.topbar .help b{font-weight:700}

.logo{left:160px;top:60px;font-family:"Calistoga",serif;font-size:46px;color:var(--brand-yellow);letter-spacing:1px;line-height:1}
.search{left:508px;top:54px;width:244px;height:32px;border:1px solid #bbb;border-radius:16px;background:#f4f4f4;font-size:12px;color:#555;padding:10px 0 0 18px}
.search .btn{position:absolute;right:2px;top:2px;width:26px;height:26px;border-radius:50%;background:var(--brand-blue);display:flex;align-items:center;justify-content:center}
.account{left:869px;top:60px;display:flex;align-items:center;gap:20px;font-size:14px;color:#333;letter-spacing:.5px}
.account span{display:flex;align-items:center;gap:6px}
.cart-count{position:absolute;right:-6px;top:-4px;width:13px;height:13px;border-radius:50%;background:var(--brand-blue);color:#fff;font-size:9px;text-align:center;line-height:13px}
.navline{left:509px;top:102px;width:690px;height:1px;background:#ddd}
.nav{left:514px;top:114px;display:flex;gap:0;font-size:14px;color:#222;letter-spacing:.3px}
.nav a{color:inherit;text-decoration:none;margin-right:38px;display:flex;align-items:center;gap:4px}
.nav a.active{color:var(--brand-blue);font-weight:700}

.crumbs{left:0;top:141px;width:1199px;height:37px;background:var(--soft);font-size:12px;color:#222}
.crumbs .row{position:absolute;left:162px;top:13px;display:flex;align-items:center;gap:14px}
.crumbs .current{color:var(--brand-blue)}

.page-title{left:0;width:1199px;top:250px;text-align:center;font-size:39px}
.back{left:161px;top:312px;font-size:12px;color:#333}
.order-label{left:161px;top:332px;font-size:15px}

.order-table{left:161px;top:370px;width:623px;border:1px solid var(--line);border-top:none}
.order-head{height:45px;background:var(--brand-blue);color:#fff;position:relative;font-family:"Calistoga",serif;font-size:15px}
.order-head span{position:absolute;top:13px}
.item{height:124px;position:relative;border-bottom:1px solid var(--line)}
.thumb{position:absolute;left:25px;top:23px;width:71px;height:78px;border:3px solid #eee;background:linear-gradient(#f7f7f7,#e4e4e4)}
.thumb i{position:absolute;left:12px;top:10px;width:42px;height:52px;border-radius:8px 8px 4px 4px;background:#1a1a1a}
.item .name{position:absolute;left:112px;top:30px;font-size:15px}
.item .desc{position:absolute;left:112px;top:58px;width:240px;font-size:12px;line-height:18px;color:#555}
.item .cell{position:absolute;top:56px;font-size:11px;color:#333}
.sums{background:var(--soft);height:76px;position:relative;font-size:12px;color:#444}
.sums div{position:absolute;left:25px;right:27px;display:flex;justify-content:space-between}
.grand{height:37px;position:relative;font-size:12px;color:#444}
.grand div{position:absolute;left:25px;right:27px;top:11px;display:flex;justify-content:space-between}

.side{left:814px;top:370px;width:225px;border:1px solid #eee}
.side .block{padding:17px 0 17px 23px;font-size:12px;color:#555;line-height:18px}
.side .block + .block{border-top:1px solid #eee}
.side h3{font-size:15px;margin-bottom:8px}
.side .status{color:#333;font-weight:500;margin-bottom:3px}
.side p{margin-bottom:3px}

.footer{left:0;top:784px;width:1199px;height:365px;background:var(--footer);color:#eee}
.footer .tear{position:absolute;left:0;top:-8px}
.foot-logo{left:162px;top:148px;font-family:"Calistoga",serif;font-size:38px;color:#fff;letter-spacing:1px}
.social{left:224px;top:209px;display:flex;gap:8px}
.social i{width:30px;height:30px;border:1.5px solid #ddd;border-radius:50%}
.fcol h4{font-family:"Calistoga",serif;font-weight:400;font-size:19px;color:#fff}
.fcol h4::after{content:"";display:block;width:35px;height:3px;background:var(--brand-yellow);margin-top:10px}
.links{list-style:none;margin-top:16px;font-size:14px}
.links li{height:27px}
.links li::before{content:"»";margin-right:8px;font-size:12px}
.contact{font-size:14px;line-height:22px}
.contact .item2{display:flex;gap:8px;margin-top:14px}
.contact b{font-weight:700;display:block}
.news p{font-size:13px;line-height:22px;margin-top:16px;width:222px}
.news .field{margin-top:18px;width:221px;height:38px;background:#fff;position:relative;color:#555;font-family:"Calistoga",serif;font-size:13px;padding:11px 0 0 10px}
.news .field .go{position:absolute;right:0;top:0;width:39px;height:38px;background:var(--brand-yellow);display:flex;align-items:center;justify-content:center}

.bottombar{left:0;top:1149px;width:1199px;height:51px;background:var(--brand-blue);color:#eef;font-size:14px}
.bottombar .copy{left:163px;top:16px}
.bottombar .pay{left:648px;top:16px}
.cards{left:798px;top:13px;display:flex;gap:9px}
.cards i{width:40px;height:25px;border-radius:2px;background:#fff}
.cards i.dark{background:#1e3a6a}
.cards i.mid{background:#2f77b8}
</style>
</head>
<body>

<div class="abs topbar">
  <span class="abs welcome">Welcome To TORVELIN!</span>
  <span class="abs help">
    <svg width="16" height="12" viewBox="0 0 16 12"><rect width="16" height="12" fill="#fff"/><path d="M0 0 L8 7 L16 0" fill="none" stroke="#000" stroke-width="1.5"/></svg>
    <b>Need help?</b> help@torvelin.example
  </span>
</div>

<div class="abs logo">TORVELIN</div>
<div class="abs search">Search Here
  <span class="btn"><svg width="13" height="13" viewBox="0 0 13 13"><circle cx="5.5" cy="5.5" r="4" fill="none" stroke="#fff" stroke-width="1.6"/><path d="M8.5 8.5 L12 12" stroke="#fff" stroke-width="1.6"/></svg></span>
</div>
<div class="abs account">
  <span><svg width="16" height="18" viewBox="0 0 16 18"><circle cx="8" cy="5" r="3.5" fill="none" stroke="#333" stroke-width="1.5"/><path d="M1 17 V12 Q1 9.5 4 9.5 H12 Q15 9.5 15 12 V17 Z" fill="none" stroke="#333" stroke-width="1.5"/></svg>SIGN IN</span>
  <span style="position:relative">CART
    <svg width="26" height="22" viewBox="0 0 26 22"><path d="M1 2 H5 L8 14 H21 L24 5 H6" fill="none" stroke="#333" stroke-width="1.8"/><circle cx="10" cy="18.5" r="2" fill="#333"/><circle cx="19" cy="18.5" r="2" fill="#333"/></svg>
    <span class="cart-count">0</span>
  </span>
</div>
<div class="abs navline"></div>
<nav class="abs nav">
  <a class="active">HOME</a>
  <a>WOMEN <svg width="9" height="6" viewBox="0 0 9 6"><path d="M1 1 L4.5 4.5 L8 1" fill="none" stroke="#222" stroke-width="1.6"/></svg></a>
  <a>MEN <svg width="9" height="6" viewBox="0 0 9 6"><path d="M1 1 L4.5 4.5 L8 1" fill="none" stroke="#222" stroke-width="1.6"/></svg></a>
  <a>ABOUT</a>
  <a>CONTACT</a>
  <a>CATALOG</a>
</nav>

<div class="abs crumbs">
  <div class="row"><span>HOME</span><span>»</span><span>MY ACCOUNT</span><span>»</span><span class="current">ORDER #1234</span></div>
</div>

<h1 class="abs heading page-title">Order #1234</h1>
<div class="abs back">Return to Account Details</div>
<div class="abs heading order-label">ORDER #1234</div>

<div class="abs order-table">
  <div class="order-head">
    <span style="left:25px">Product</span>
    <span style="left:386px">Price</span>
    <span style="left:460px">Quantity</span>
    <span style="left:562px">Total</span>
  </div>
  <div class="item">
    <div class="thumb" role="img" aria-label="Black printed T-shirt product photo"><i></i></div>
    <div class="heading name">Lorem Ipsum Is Text</div>
    <div class="desc">Lorem Ipsum is simply dummy text of the printing and typesetting industry.</div>
    <span class="cell" style="left:386px">$11.95</span>
    <span class="cell" style="left:488px">1</span>
    <span class="cell" style="left:562px">$11.95</span>
  </div>
  <div class="sums">
    <div style="top:18px"><span>Subtotal</span><span>$11.95</span></div>
    <div style="top:45px"><span>Shipping Standard</span><span>$0.00</span></div>
  </div>
  <div class="grand"><div><span>Subtotal</span><span>$11.95</span></div></div>
</div>

<aside class="abs side">
  <div class="block">
    <h3 class="heading">Account Details</h3>
    <p class="status">Payment Status : Pending</p>
    <p>Mr. Lorem Ipsum</p>
    <p style="margin-top:5px">123, Lorem ipsum dolor sit amet, Newyork, 123456</p>
    <p style="margin-top:7px">1234567890</p>
  </div>
  <div class="block">
    <h3 class="heading">Account Details</h3>
    <p class="status">Payment Status : Pending</p>
    <p>Mr. Lorem Ipsum</p>
    <p style="margin-top:5px">123, Lorem ipsum dolor sit amet, Newyork, 123456</p>
    <p style="margin-top:7px">1234567890</p>
  </div>
</aside>

<footer class="abs footer">
  <svg class="tear" width="1199" height="12" viewBox="0 0 1199 12" preserveAspectRatio="none">
    <path fill="#333" d="M0 12 V7 L20 6 L35 8 L60 5 L80 7 L110 6 L130 8 L160 5 L190 7 L215 6 L240 8 L270 5 L300 7 L330 6 L350 8 L380 5 L410 7 L440 6 L470 8 L500 5 L530 7 L560 6 L590 8 L620 5 L650 7 L680 6 L710 8 L740 5 L770 7 L800 6 L830 8 L860 5 L890 7 L920 6 L950 8 L980 5 L1010 7 L1040 6 L1070 8 L1100 5 L1130 7 L1160 6 L1180 8 L1199 4 V12 Z"/>
  </svg>
  <div class="abs foot-logo">TORVELIN</div>
  <div class="abs social"><i></i><i></i></div>

  <div class="abs fcol" style="left:410px;top:82px">
    <h4>Quick Links</h4>
    <ul class="links">
      <li>Home</li><li>About</li><li>Contact</li><li>Catalog</li><li>Shipping</li><li>Returns</li>
    </ul>
  </div>

  <div class="abs fcol contact" style="left:566px;top:82px">
    <h4>Contact Details</h4>
    <div class="item2" style="margin-top:16px">
      <svg width="12" height="16" viewBox="0 0 12 16"><path d="M6 0 A6 6 0 0 0 0 6 C0 10 6 16 6 16 C6 16 12 10 12 6 A6 6 0 0 0 6 0 Z" fill="#fff"/><circle cx="6" cy="6" r="2.2" fill="#333"/></svg>
      <span>123 Building Name, Street<br>City Name, State 123456</span>
    </div>
    <div class="item2">
      <svg width="14" height="14" viewBox="0 0 14 14"><path d="M3 0 L5.5 3.5 L4 5.5 Q5.5 8.5 8.5 10 L10.5 8.5 L14 11 L12 14 Q4 13 0 2 Z" fill="#fff"/></svg>
      <span><b>PHONE</b>+1 123 456 7890</span>
    </div>
    <div class="item2">
      <svg width="15" height="11" viewBox="0 0 16 12" style="margin-top:4px"><rect width="16" height="12" fill="#fff"/><path d="M0 0 L8 7 L16 0" fill="none" stroke="#333" stroke-width="1.5"/></svg>
      <span><b>EMAIL</b>help@torvelin.example</span>
    </div>
  </div>

  <div class="abs fcol news" style="left:817px;top:82px">
    <h4>Newsletter Subscribe</h4>
    <p>Lorem ipsum dolor amet consetuer ading elit sed diam nonummy.</p>
    <div class="field">Email Address
      <span class="go"><svg width="17" height="17" viewBox="0 0 17 17"><path d="M17 0 L0 7 L6 10 L7 17 L10 12 Z" fill="#222"/></svg></span>
    </div>
  </div>
</footer>

<div class="abs bottombar">
  <span class="abs copy">Copyright 2020 Torvelin. All Rights Reserved.</span>
  <span class="abs pay">Payment We Accept</span>
  <div class="abs cards"><i></i><i></i><i></i><i class="mid"></i><i class="dark"></i></div>
</div>

</body>
</html>
```